Grace Fellowship Ardmore, MS needs a Business Card design

We are in the process of rebranding our church with a new logo with a fresh appeal to younger families moving into our community and joining our church. We are in need of a new business card design and would like to see 2 sided designs that incorporate the web color 00cccc.

We would like to have our logo, church name (grace fellowship ardmore) and our what we are about (gather.grow.serve.) in addition to the following information:
Name: Dr. Samuel Whitfield
Title: Teaching Pastor
Phone: 6015550142
Email: swhitfield@gfcardmore.example
Website: www.gfcardmore.example
Address: 714 N Elmwood Avenue Ardmore, MS 39187

Target Market(s)

Ardmore, MS is a bedroom community outside of Jackson that is experiencing exponential growth with young professionals/young families moving in. We are making a lot of changes to reach this demographic while still honoring and continuing to reach those who have lived here for a while.

Industry/Entity Type

Church

Contact Information for Business Card

Grace Fellowship Ardmore - gather.grow.serve.
Dr. Samuel Whitfield
Teaching Pastor
6015550142
swhitfield@gfcardmore.example
www.gfcardmore.example
714 N Elmwood Avenue
Ardmore, MS 39187

Font styles to use
Sans Serif

```html
<!DOCTYPE html>
<html lang="en">
<head>
<meta charset="utf-8">
<title>Grace Fellowship Ardmore – Business Card</title>
<link rel="stylesheet" href="https://fonts.googleapis.com/css2?family=Work+Sans:wght@400;500;600&display=swap">
<style>
  :root {
    --page: #2a2a2b;
    --card: #151516;
    --card-edge: #1d1d1e;
    --white: #f4f4f4;
    --muted: #8a8a8c;
    --teal: #00cccc;
    --teal-soft: #9fe3de;
  }
  * { box-sizing: border-box; margin: 0; padding: 0; }
  html, body {
    width: 1200px; height: 900px; overflow: hidden;
    background: var(--page);
    font-family: "Work Sans", sans-serif;
    color: var(--white);
  }
  .canvas {
    position: relative; width: 1200px; height: 900px;
    display: flex; flex-direction: column; align-items: center; justify-content: center; gap: 50px;
  }
  .card {
    position: relative; width: 640px; height: 366px;
    background: linear-gradient(135deg, var(--card-edge), var(--card));
    box-shadow: 0 2px 0 #3a3a3b, 0 14px 30px rgba(0,0,0,.45);
  }
  /* Front */
  .card-front { display: flex; flex-direction: column; align-items: center; justify-content: center; }
  .front-name {
    font-size: 32px; font-weight: 400; letter-spacing: 1.5px; text-transform: uppercase; white-space: nowrap;
  }
  .front-tagline { margin-top: 6px; font-size: 17px; font-weight: 500; letter-spacing: 1px; }
  /* Back */
  .card-back { display: flex; align-items: center; }
  .brand {
    width: 300px; flex: none; display: flex; flex-direction: column; align-items: center; gap: 26px;
  }
  .brand-dot {
    width: 84px; height: 84px; border-radius: 50%;
    background: linear-gradient(135deg, var(--teal-soft), var(--teal));
  }
  .brand-name {
    font-size: 17px; font-weight: 400; letter-spacing: .8px; text-transform: uppercase;
    color: var(--muted); white-space: nowrap;
  }
  .divider { width: 2px; height: 180px; flex: none; background: var(--white); }
  .contact { padding-left: 28px; }
  .contact-name { font-size: 24px; font-weight: 600; white-space: nowrap; }
  .contact-title { font-size: 15px; letter-spacing: .5px; margin-bottom: 14px; }
  .contact-address { font-size: 15px; line-height: 1.35; letter-spacing: .5px; margin-bottom: 10px; }
  .contact-line { display: flex; align-items: center; gap: 10px; font-size: 15px; letter-spacing: .5px; line-height: 1.65; white-space: nowrap; }
  .contact-line svg { width: 12px; height: 12px; flex: none; }
</style>
</head>
<body>
<main class="canvas">
  <section class="card card-front">
    <p class="front-name">Grace Fellowship Ardmore</p>
    <p class="front-tagline">gather. grow. serve.</p>
  </section>

  <section class="card card-back">
    <div class="brand">
      <span class="brand-dot"></span>
      <p class="brand-name">Grace Fellowship Ardmore</p>
    </div>
    <span class="divider"></span>
    <div class="contact">
      <p class="contact-name">Dr. Samuel Whitfield</p>
      <p class="contact-title">Teaching Pastor</p>
      <p class="contact-address">714 N Elmwood Avenue<br>Ardmore, MS 39187</p>
      <p class="contact-line">
        <svg viewBox="0 0 12 12" fill="var(--white)"><path d="M2.5 0.8 4.3 0.5 5.2 3 4 4c.6 1.5 1.8 2.7 3.3 3.3l1-1.2 2.5.9-.3 1.8C10 10.9 8.8 11.4 7.7 11 4.6 9.9 2.1 7.4 1 4.3.6 3.2 1.1 2 2.5.8z"/></svg>
        6015550142
      </p>
      <p class="contact-line">
        <svg viewBox="0 0 12 12" fill="none" stroke="var(--white)" stroke-width="1.2"><rect x="1" y="2.5" width="10" height="7"/><path d="M1 2.5 6 6.5 11 2.5"/></svg>
        swhitfield@gfcardmore.example
      </p>
      <p class="contact-line">
        <svg viewBox="0 0 12 12" fill="none" stroke="var(--white)" stroke-width="1"><circle cx="6" cy="6" r="5"/><ellipse cx="6" cy="6" rx="2.2" ry="5"/><path d="M1 6h10M2 3.5h8M2 8.5h8"/></svg>
        www.gfcardmore.example
      </p>
    </div>
  </section>
</main>
</body>
</html>
```